Web design for Modeling agency

We are looking for re-designing our modeling agency website.
Current website: brisamodels.com our competitor: QRTmodels.com
http://ravonmodel.fr/
https://www.dunforthmanagement.com/models/
https://www.hendra-models.de
https://www.fennmanagement.co.uk
https://www.vantrimodel.com
https://www.brackenfordmodels.com

Target Market(s)

modeling agency

Industry/Entity Type

modeling agency

Number of Pages Required

5+ page

Font styles to use
Other font styles liked:
• base on logo guidline

Requirements
Nice to have
• current website: brisamodels.com our competitor: QRTmodels.com

```html
<!DOCTYPE html>
<html lang="en">
<head>
<meta charset="utf-8">
<title>Brisa Models – Web Design</title>
<link href="https://fonts.googleapis.com/css2?family=Roboto:wght@300;400;500;700&family=Outfit:wght@700;800&display=swap" rel="stylesheet">
<style>
:root{
  --board:#dcdcdc;
  --paper:#ffffff;
  --cream:#f6f2ec;
  --tan:#b8917a;
  --ink:#111111;
  --text:#222222;
  --muted:#8a8a8a;
  --photo-warm:#c9a88a;
  --photo-dark:#3d3a3a;
}
*{margin:0;padding:0;box-sizing:border-box}
html,body{width:1044px;height:1200px;overflow:hidden;background:var(--board)}
body{font-family:"Roboto",Arial,sans-serif;color:var(--text)}
.board{position:absolute;left:0;top:0;width:1792px;height:2060px;transform:scale(.5826);transform-origin:0 0}
.abs{position:absolute}
.photo{position:absolute;display:block}

/* splash */
.splash{position:absolute;left:130px;top:135px;width:731px;height:393px;
  background:radial-gradient(circle at 40% 40%,#f8f5f1,#f3ede4);box-shadow:0 0 2px rgba(0,0,0,.08)}
.splash .brand{position:absolute;left:0;right:0;top:140px;text-align:center;font-weight:300;font-size:56px;letter-spacing:4px;color:var(--tan)}
.cities{position:absolute;left:0;right:0;top:229px;display:flex;justify-content:center;gap:22px;font-size:10.5px;font-weight:500;color:#333;letter-spacing:.3px}

/* home page */
.page{position:absolute;left:931px;top:135px;width:731px;height:1793px;background:var(--paper);box-shadow:0 0 2px rgba(0,0,0,.08)}
.topbar .brand{position:absolute;left:68px;top:7px;font-weight:300;font-size:26px;letter-spacing:2px;color:var(--tan)}
.nav{position:absolute;right:68px;top:16px;display:flex;gap:19px;font-size:9.5px;font-weight:500;color:#111;align-items:center}
.hero{left:0;top:45px;width:731px;height:353px;background:linear-gradient(100deg,#9a7660 0%,#c8a084 35%,#e4c9ad 60%,#caa588 100%)}
.hero-brand{position:absolute;left:68px;top:190px;font-weight:300;font-size:50px;letter-spacing:4px;color:#fff}
.h2{position:absolute;left:0;right:0;text-align:center;font-family:"Outfit",Arial,sans-serif;font-weight:800;color:var(--ink)}
.sub{position:absolute;left:0;right:0;top:479px;text-align:center;font-size:8px;color:var(--muted)}
.name{position:absolute;width:143px;text-align:center;font-size:10px;font-weight:500;color:#111}
.arrow{position:absolute;top:588px}
.vt{position:absolute;left:631px;font-size:9.5px;font-weight:700;color:#111}
.vs{position:absolute;left:631px;font-size:6.5px;color:#666}
.h3{position:absolute;font-family:"Outfit",Arial,sans-serif;font-weight:700;font-size:19px;color:var(--ink)}
.latest{position:absolute;right:68px;top:1158px;font-size:9.5px;font-weight:500;color:var(--tan);display:flex;align-items:center;gap:5px}
.ptitle{position:absolute;font-size:9.5px;font-weight:500;color:#111}
.psub{position:absolute;font-size:8px;color:var(--muted)}
.foot-brand{position:absolute;left:0;right:0;top:1662px;text-align:center;font-weight:300;font-size:38px;letter-spacing:3px;color:var(--tan)}
.flinks{position:absolute;top:1731px;font-size:8.5px;font-weight:700;color:#111;display:flex;gap:14px}
.social{position:absolute;left:596px;top:1732px;display:flex;gap:10px}
.social span{width:8px;height:8px;border-radius:50%;background:#111;display:block}
.copy{position:absolute;left:0;right:0;top:1759px;text-align:center;font-size:7.5px;color:#333}
.code{position:absolute;left:692px;top:1760px;font-size:6.5px;color:var(--muted)}
</style>
</head>
<body>
<div class="board">

  <section class="splash">
    <div class="photo" role="img" aria-label="Faint pattern of overlapping beige circles" style="inset:0"></div>
    <div class="brand">BRISA</div>
    <div class="cities"><span>LONDON</span><span>|</span><span>PARIS</span><span>|</span><span>ISTANBUL</span><span>|</span><span>MILAN</span><span>|</span><span>ATHENS</span><span>|</span><span>DUBAI</span></div>
  </section>

  <section class="page">
    <header class="topbar">
      <div class="brand">BRISA</div>
      <nav class="nav">
        <span>Vantri Atlanta</span><span>Men</span><span>Women</span><span>Development</span><span>Talent</span><span>Video</span><span>About</span><span>News</span>
        <svg width="10" height="10" viewBox="0 0 10 10"><circle cx="4" cy="4" r="3" fill="none" stroke="#111" stroke-width="1.6"/><line x1="6.2" y1="6.2" x2="9" y2="9" stroke="#111" stroke-width="1.8"/></svg>
        <svg width="10" height="9" viewBox="0 0 10 9"><rect y="0" width="10" height="1.6" fill="#111"/><rect y="3.7" width="10" height="1.6" fill="#111"/><rect y="7.4" width="10" height="1.6" fill="#111"/></svg>
      </nav>
    </header>

    <div class="photo hero" role="img" aria-label="Model in floral top standing on a sunlit city street"></div>
    <div class="hero-brand">BRISA</div>

    <h2 class="h2" style="top:444px;font-size:28px">ON STAY</h2>
    <div class="sub">WOMEN // MEN // VIEW ALL</div>
    <svg class="arrow" style="left:27px" width="14" height="24" viewBox="0 0 14 24"><polyline points="12,2 2,12 12,22" fill="none" stroke="#888" stroke-width="2"/></svg>
    <svg class="arrow" style="left:690px" width="14" height="24" viewBox="0 0 14 24"><polyline points="2,2 12,12 2,22" fill="none" stroke="#888" stroke-width="2"/></svg>
    <div class="photo" role="img" aria-label="Male model in leather jacket seated on a wooden pallet" style="left:68px;top:509px;width:143px;height:181px;background:linear-gradient(#6a6766,#4a3a30)"></div>
    <div class="photo" role="img" aria-label="Portrait of female model with curly hair" style="left:219px;top:520px;width:143px;height:160px;background:linear-gradient(#b08f7e,#8a6654)"></div>
    <div class="photo" role="img" aria-label="Female model in rust knit dress on dark background" style="left:369px;top:509px;width:143px;height:181px;background:linear-gradient(#1f2d35,#5a3324)"></div>
    <div class="photo" role="img" aria-label="Beauty portrait of blonde female model" style="left:520px;top:520px;width:143px;height:160px;background:linear-gradient(#a2806c,#d9b8a1)"></div>
    <div class="name" style="left:68px;top:701px">MALCOLM</div>
    <div class="name" style="left:219px;top:691px">MALCOLM</div>
    <div class="name" style="left:369px;top:701px">MALCOLM</div>
    <div class="name" style="left:520px;top:691px">MALCOLM</div>

    <h2 class="h2" style="top:759px;font-size:28px">VIDEOS</h2>
    <div class="photo" role="img" aria-label="Three smiling female models posing together" style="left:9px;top:808px;width:525px;height:286px;background:linear-gradient(90deg,#c7a888,#b08c6c 50%,#d4b896)"></div>
    <svg class="abs" style="left:249px;top:928px" width="46" height="46" viewBox="0 0 46 46"><circle cx="23" cy="23" r="21" fill="none" stroke="#fff" stroke-width="3"/><polygon points="18,14 32,23 18,32" fill="#fff"/></svg>

    <div class="photo" role="img" aria-label="Video thumbnail of model" style="left:553px;top:808px;width:67px;height:50px;background:#a89080"></div>
    <div class="photo" role="img" aria-label="Video thumbnail of model" style="left:553px;top:867px;width:67px;height:50px;background:#8a7264"></div>
    <div class="photo" role="img" aria-label="Video thumbnail of model" style="left:553px;top:926px;width:67px;height:50px;background:#6e6660"></div>
    <div class="photo" role="img" aria-label="Video thumbnail of model" style="left:553px;top:985px;width:67px;height:50px;background:#6a6488"></div>
    <div class="photo" role="img" aria-label="Video thumbnail of model" style="left:553px;top:1044px;width:67px;height:50px;background:#9c7c78"></div>
    <div class="vt" style="top:822px">Lorem ipsum dolor</div><div class="vs" style="top:839px">sed do eiusmod</div>
    <div class="vt" style="top:881px">Lorem ipsum dolor</div><div class="vs" style="top:898px">sed do eiusmod</div>
    <div class="vt" style="top:940px">Lorem ipsum dolor</div><div class="vs" style="top:957px">sed do eiusmod</div>
    <div class="vt" style="top:999px">Lorem ipsum dolor</div><div class="vs" style="top:1016px">sed do eiusmod</div>
    <div class="vt" style="top:1058px">Lorem ipsum dolor</div><div class="vs" style="top:1075px">sed do eiusmod</div>

    <h3 class="h3" style="left:68px;top:1153px">EXPLORE OUR WORLD</h3>
    <div class="latest">LATEST NEWS <svg width="9" height="9" viewBox="0 0 10 10"><circle cx="5" cy="5" r="5" fill="#b8917a"/><polyline points="4,2.5 6.5,5 4,7.5" fill="none" stroke="#fff" stroke-width="1.5"/></svg></div>
    <div class="photo" role="img" aria-label="Smiling female model among pink blossoms" style="left:68px;top:1198px;width:191px;height:137px;background:linear-gradient(#d7a2a0,#c99a86)"></div>
    <div class="photo" role="img" aria-label="Male model with travel bag on a city street" style="left:270px;top:1198px;width:191px;height:137px;background:linear-gradient(#3d4f78,#5a4a42)"></div>
    <div class="photo" role="img" aria-label="Blonde female model among white flowers" style="left:472px;top:1198px;width:191px;height:137px;background:linear-gradient(#7d8a4c,#d9c4a4)"></div>
    <div class="ptitle" style="left:68px;top:1352px">Lorem ipsum dolor sit amet</div><div class="psub" style="left:68px;top:1369px">Sed ut perspiciatis</div>
    <div class="ptitle" style="left:270px;top:1352px">Lorem ipsum dolor sit amet</div><div class="psub" style="left:270px;top:1369px">Sed ut perspiciatis</div>
    <div class="ptitle" style="left:472px;top:1352px">Lorem ipsum dolor sit amet</div><div class="psub" style="left:472px;top:1369px">Sed ut perspiciatis</div>

    <h3 class="h3" style="left:303px;top:1429px">FOLLOW US</h3>
    <svg class="abs" style="left:412px;top:1433px" width="15" height="15" viewBox="0 0 15 15"><circle cx="7.5" cy="7.5" r="6.3" fill="none" stroke="#111" stroke-width="1.6"/></svg>
    <div class="photo" role="img" aria-label="Male model in white by the sea" style="left:5px;top:1467px;width:141px;height:158px;background:linear-gradient(#3b7fb8,#d9dde0)"></div>
    <div class="photo" role="img" aria-label="Male model with sweater over shoulders on street" style="left:151px;top:1467px;width:140px;height:158px;background:linear-gradient(#8a7860,#3a3430)"></div>
    <div class="photo" role="img" aria-label="Female model with long wavy hair" style="left:296px;top:1467px;width:140px;height:158px;background:linear-gradient(#c4ad94,#4a362c)"></div>
    <div class="photo" role="img" aria-label="Female model in sunglasses seated outdoors" style="left:441px;top:1467px;width:141px;height:158px;background:linear-gradient(#6a6048,#2e2e30)"></div>
    <div class="photo" role="img" aria-label="Male model with bicycle in the city" style="left:586px;top:1467px;width:141px;height:158px;background:linear-gradient(#4a4a4e,#2a2a30)"></div>

    <div class="foot-brand">BRISA</div>
    <div class="flinks" style="left:68px">LANGUAGES</div>
    <div class="flinks" style="left:186px"><span>BECOME A MODEL</span><span>|</span><span>IMPRESSUM</span><span>|</span><span>DATA PROTECTION</span><span>|</span><span>DISCLAMER</span></div>
    <div class="social"><span></span><span></span><span></span><span></span></div>
    <div class="copy">Copyrights © brisamodels 2021 | Allrights Reserved</div>
    <div class="code">C37</div>
  </section>

</div>
</body>
</html>
```